Canadian Christian Church needs design for new sermon series

A graphic design for our series and an invitation card to invite people to the series. Check design brief for more detailed information. Target audience: young families and young adults. Looking for a creative design that will get people's attention and create interest. See design brief for copy of design purchased for previous series.
entered Apr 4 incorrectly. Need a week to receive and review designs, and today is Apr 2/19. Thanks!
young families and young adults

```html
<!DOCTYPE html>
<html lang="en">
<head>
<meta charset="utf-8">
<title>Maple Ridge Family Church – Messy Sermon Series</title>
<link rel="stylesheet" href="https://fonts.googleapis.com/css2?family=Josefin+Sans:wght@400;600&family=Questrial&family=Roboto+Condensed:wght@300;400&family=Roboto:wght@400&display=swap">
<style>
  :root {
    --ink: #1d1d1d;
    --accent: #c6825a;
    --bullet-light: #d8714a;
    --bullet-dark: #a9432a;
    --rubble-top: #c9b3ab;
    --rubble-mid: #9c7a6e;
    --rubble-deep: #7d5a4e;
    --band: rgba(128, 74, 58, 0.88);
    --paper: #ffffff;
  }
  html, body {
    margin: 0;
    padding: 0;
    overflow: hidden;
    background: var(--paper);
  }
  .card {
    position: relative;
    width: 1200px;
    height: 943px;
    overflow: hidden;
    background: var(--paper);
    font-family: "Josefin Sans", sans-serif;
    color: var(--ink);
  }
  .sc {
    font-variant: small-caps;
    font-weight: 400;
  }

  /* Header */
  .headline {
    position: absolute;
    left: 87px;
    width: 1026px;
    top: 86px;
    margin: 0;
    font-size: 37px;
    line-height: 1;
    letter-spacing: 0.5px;
    white-space: nowrap;
    display: flex;
    justify-content: space-between;
  }
  .headline .series { color: var(--accent); }
  .headline-rule {
    position: absolute;
    left: 87px;
    top: 137px;
    width: 1026px;
    height: 4px;
    background: var(--accent);
  }

  /* Section headings */
  .section-title {
    position: absolute;
    margin: 0;
    color: var(--accent);
    font-size: 37px;
    line-height: 1;
    letter-spacing: 1px;
  }
  .features-title { left: 87px; top: 168px; }
  .location-title { left: 87px; top: 391px; }
  .dates-title { right: 88px; top: 169px; }

  .dot {
    display: inline-block;
    width: 24px;
    height: 24px;
    border-radius: 50%;
    background: radial-gradient(circle at 38% 35%, var(--bullet-light), var(--bullet-dark));
  }

  /* Features */
  .features {
    position: absolute;
    left: 86px;
    top: 216px;
    margin: 0;
    padding: 0;
    list-style: none;
    font-size: 26px;
    line-height: 36px;
  }
  .features li {
    position: relative;
    padding-left: 35px;
    margin-bottom: 10px;
  }
  .features .dot {
    position: absolute;
    left: 0;
    top: 4px;
  }

  /* Location */
  .pin {
    position: absolute;
    left: 100px;
    top: 437px;
    width: 56px;
    height: 100px;
  }
  .address {
    position: absolute;
    left: 172px;
    top: 445px;
    margin: 0;
    font-family: "Questrial", sans-serif;
    font-style: normal;
    font-size: 22px;
    line-height: 29px;
    letter-spacing: 0.8px;
  }

  /* Schedule */
  .schedule {
    position: absolute;
    right: 88px;
    top: 214px;
    margin: 0;
    padding: 0;
    list-style: none;
    font-size: 26px;
  }
  .schedule li {
    display: grid;
    grid-template-columns: auto 24px 120px;
    column-gap: 14px;
    align-items: center;
    height: 45.8px;
  }
  .schedule .talk { text-align: right; }
  .schedule .date { padding-left: 0; }

  /* Imagery and band */
  .rubble {
    position: absolute;
    left: 0;
    top: 560px;
    width: 1200px;
    height: 383px;
    background: linear-gradient(to bottom,
      rgba(255,255,255,0) 0%,
      var(--rubble-top) 14%,
      var(--rubble-mid) 45%,
      var(--rubble-deep) 100%);
  }
  .service-band {
    position: absolute;
    left: 0;
    top: 685px;
    width: 1200px;
    height: 171px;
    background: var(--band);
    color: var(--paper);
  }
  .service-lead {
    position: absolute;
    left: 87px;
    top: 20px;
    margin: 0;
    font-family: "Roboto Condensed", sans-serif;
    font-weight: 300;
    font-size: 44px;
    line-height: 1;
    letter-spacing: 3.2px;
    text-transform: uppercase;
    white-space: nowrap;
  }
  .service-time {
    position: absolute;
    left: 85px;
    top: 62px;
    margin: 0;
    font-family: "Roboto Condensed", sans-serif;
    font-weight: 400;
    font-size: 84px;
    line-height: 1;
    letter-spacing: 1px;
    text-transform: uppercase;
    white-space: nowrap;
  }
  .contact {
    position: absolute;
    right: 88px;
    top: 22px;
    margin: 0;
    text-align: right;
    font-family: "Roboto", sans-serif;
    font-style: normal;
    font-size: 31px;
    line-height: 36.5px;
    letter-spacing: -0.3px;
  }
</style>
</head>
<body>
<main class="card">
  <h1 class="headline sc">
    <span>Maple Ridge Family Church</span>
    <span class="series">Messy</span>
    <span>sermon series begins</span>
  </h1>
  <div class="headline-rule"></div>

  <h2 class="section-title features-title sc">Featuring:</h2>
  <ul class="features sc">
    <li><span class="dot"></span>Staffed nursery and children’s program<br>every Sunday</li>
    <li><span class="dot"></span>Coffee &amp; snacks</li>
    <li><span class="dot"></span>Everyone welcome</li>
  </ul>

  <h2 class="section-title location-title sc">Find us at:</h2>
  <svg class="pin" viewBox="0 0 56 100" aria-hidden="true">
    <path d="M28 2 C13 2 3 13 3 27 C3 44 28 72 28 72 C28 72 53 44 53 27 C53 13 43 2 28 2 Z" fill="#c6825a"/>
    <circle cx="28" cy="26" r="10" fill="#ffffff"/>
    <path d="M17 72 C7 74 3 79 3 84 C3 92 14 97 28 97 C42 97 53 92 53 84 C53 79 49 74 39 72" fill="none" stroke="#c6825a" stroke-width="5"/>
  </svg>
  <address class="address">1875 Cedar Line<br>West Brookfield,<br>ON L4X 2M8</address>

  <h2 class="section-title dates-title sc">Save the date</h2>
  <ul class="schedule sc">
    <li><span class="talk">“We Made This Mess”</span><span class="dot"></span><span class="date">April 28th</span></li>
    <li><span class="talk">“Bless in the Mess”</span><span class="dot"></span><span class="date">May 5th</span></li>
    <li><span class="talk">“Born into the Mess”</span><span class="dot"></span><span class="date">May 12th</span></li>
    <li><span class="talk">“Messy Work”</span><span class="dot"></span><span class="date">May 19th</span></li>
    <li><span class="talk">“Messy Church”</span><span class="dot"></span><span class="date">May 26th</span></li>
    <li><span class="talk">“Messy Hospitality”</span><span class="dot"></span><span class="date">June 2nd</span></li>
    <li><span class="talk">TBD</span><span class="dot"></span><span class="date">June 9th</span></li>
    <li><span class="talk">“Messy within Boundaries”</span><span class="dot"></span><span class="date">June 16th</span></li>
  </ul>

  <div class="rubble" role="img" aria-label="Photo of a heap of rubble with a single hand reaching up out of it"></div>

  <section class="service-band">
    <p class="service-lead">Services will take&nbsp; place on</p>
    <p class="service-time">Sundays at 10:30</p>
    <address class="contact">905.555.0148<br>info@mrfamilychurch.ca<br>www.mrfamilychurch.ca</address>
  </section>
</main>
</body>
</html>
```